Business Card Design

New business, starting out small. High end residential/ commercial building company in Sydney Australia's prestigious Eastern suburbs, perfection is our motto and we want our marketing design to reflect that.

Therefore marketing towards high end clients. Looking for design concepts that will portray this image and will appeal to both male and females, prototype has been included- see images. Although we are open to ideas we have included this to give direction.

DARK Navy and white is the colour scheme, as per image provided. Logo ideas welcomed, however design is preferred simple, modern and sophisticated.

This business card will be the template and inspiration for website, t-shirt, banners etc to come so if you want the business, show us your design!

Industry/Entity Type

Marketing

Contact Information for Business Card

Company name: Tallow Ridge Building
Catch phrase: Your vision
Owner/operator: Garreth Pell
Phone: 0468172905
Website: www.tallowridgebuilding.com.au
Licence No 518294K
ABN 72 913 804
Email address
(displayed on back of card):info@tallowridgebuilding.com.au

```html
<!DOCTYPE html>
<html lang="en">
<head>
<meta charset="utf-8">
<title>Tallow Ridge Building – Business Card</title>
<link rel="stylesheet" href="https://fonts.googleapis.com/css2?family=Oswald:wght@400&family=Questrial&family=Montserrat:wght@600&display=swap">
<style>
  :root {
    --page: #ffffff;
    --navy: #0b1526;
    --navy-edge: #0e1a2e;
    --white: #ffffff;
    --soft: #e6e8ec;
    --licence: #e3a233;
    --label: #d9302a;
  }
  * { margin: 0; padding: 0; box-sizing: border-box; }
  html, body {
    width: 1200px; height: 1000px; overflow: hidden;
    background: var(--page);
  }
  .sheet {
    position: absolute; left: 16px; top: 320px;
    width: 1168px; height: 360px;
    display: flex; gap: 1px; background: var(--page);
  }
  .card {
    position: relative; width: 583px; height: 360px;
    background: linear-gradient(180deg, var(--navy-edge), var(--navy));
    color: var(--white); text-align: center;
  }
  .mark-square {
    position: absolute; left: 50%; transform: translateX(-50%);
    width: 44px; height: 44px; background: var(--soft);
  }
  .company {
    position: absolute; left: 0; right: 0;
    font-family: "Oswald", sans-serif; font-weight: 400;
    text-transform: uppercase; letter-spacing: 1px; line-height: 1;
  }
  .tagline {
    position: absolute; left: 0; right: 0;
    font-family: "Questrial", sans-serif; text-transform: uppercase;
    color: var(--soft); line-height: 1;
  }
  .website {
    position: absolute; left: 0; right: 0; top: 184px;
    font-family: "Questrial", sans-serif; font-size: 15px;
    letter-spacing: 1.2px; text-transform: uppercase; font-weight: 700;
  }
  .contact {
    position: absolute; left: 0; right: 0; top: 243px;
    font-family: "Montserrat", sans-serif; font-weight: 600;
    font-size: 12px; line-height: 15px;
  }
  .licence {
    position: absolute; left: 0; right: 0; top: 330px;
    font-family: "Questrial", sans-serif; font-size: 10px; color: var(--licence);
  }
  .email {
    position: absolute; left: 0; right: 0; top: 250px;
    font-family: "Questrial", sans-serif; font-size: 11px; letter-spacing: .4px;
  }
  .side-label {
    position: absolute; font-family: "Questrial", sans-serif;
    font-size: 19px; color: var(--label); letter-spacing: 1px;
  }
  .front .mark-square { top: 44px; }
  .front .company { top: 108px; font-size: 25px; }
  .front .tagline { top: 138px; font-size: 8px; letter-spacing: 6px; }
  .front .side-label { left: 72px; top: 298px; }
  .back .mark-square { top: 104px; }
  .back .company { top: 176px; font-size: 30px; }
  .back .tagline { top: 211px; font-size: 9px; letter-spacing: 8px; }
  .back .side-label { left: 386px; top: 308px; }
</style>
</head>
<body>
  <main class="sheet">
    <section class="card front" aria-label="Card front">
      <div class="mark-square"></div>
      <h1 class="company">Tallow Ridge Building</h1>
      <p class="tagline">‘ Built to perfection ’</p>
      <p class="website">www.tallowridgebuilding.com.au</p>
      <p class="contact">GARRETH PELL<br>046-817-2905</p>
      <span class="side-label">front</span>
      <p class="licence">Licence No 518294K ABN 72 913 804</p>
    </section>
    <section class="card back" aria-label="Card back">
      <div class="mark-square"></div>
      <h2 class="company">Tallow Ridge Building</h2>
      <p class="tagline">‘ Built to perfection ’</p>
      <p class="email">Email :- info@tallowridgebuilding.com.au</p>
      <span class="side-label">Back</span>
    </section>
  </main>
</body>
</html>
```